CopperWren Works, LLC Corporate Web Site

The goal of this web site is simple. To provide an information and corporate information site for people who click on company links from other web sites. Put simply, this web site is primarily a brochure web site for the parent business. It will contain information about the company and our products with links to those products. It will be designed as a small web site but scalable as we add more products and services to our repertoire.

Please see the PDF in the uploaded files/media for more information on colors and basic guidelines, but be creative for sure.

Target Market(s)

General

Industry/Entity Type

Technology, Software

Coding

Coded - Design and coding required

Font styles to use
Other font styles liked:
• Goliath, Roboto

Colors
FFC000
F8CF3A
FAE287
FDF2CF
FEFAEE

Requirements
Must have
• Home page template, interior template, News/Press release template
Nice to have
• Searchable
Should not have
• carousels, one-page design

```html
<!DOCTYPE html>
<html lang="en">
<head>
<meta charset="utf-8">
<title>CopperWren Works</title>
<link rel="stylesheet" href="https://fonts.googleapis.com/css2?family=Poppins:wght@400;500;600;700&display=swap">
<style>
:root{
  --orange:#ff8c00;
  --orange-soft:#f7941d;
  --ink:#222;
  --dark:#1e1e1e;
  --footer:#13171c;
  --grey:#f4f4f4;
  --white:#fff;
  --blue:#3a4fa0;
}
*{box-sizing:border-box;margin:0;padding:0}
html,body{width:1200px;height:3857px;overflow:hidden}
body{font-family:"Poppins",sans-serif;color:var(--ink);background:var(--white);position:relative}
.abs{position:absolute}
a{color:inherit;text-decoration:none}

/* header */
.site-header{top:0;left:0;width:1200px;height:120px;background:var(--white)}
.brand{font-weight:700;color:var(--orange);font-size:26px;display:flex;align-items:center;gap:10px}
.brand .dot{width:16px;height:16px;border-radius:50%;background:var(--orange)}
.site-header .brand{left:85px;top:40px}
.main-nav{left:476px;top:47px;display:flex;gap:21px;font-size:14px;font-weight:500;text-transform:uppercase}
.main-nav .active{color:var(--orange);border-bottom:2px solid var(--orange);padding-bottom:3px}

/* hero */
.hero{top:120px;left:0;width:1200px;height:585px;background:radial-gradient(ellipse at 70% 30%,#4a4540,#1d1b1a 70%)}
.hero h1{position:absolute;top:118px;width:100%;text-align:center;color:#fff;font-size:40px;line-height:50px;font-weight:700}
.hero p{position:absolute;top:248px;left:300px;width:600px;text-align:center;color:#fff;font-size:20px;line-height:29px;font-weight:500}
.btn-ghost{border:2px solid #fff;color:#fff;border-radius:6px;font-size:20px;font-weight:500;display:flex;align-items:center;justify-content:center}
.hero .btn-ghost{left:520px;top:392px;width:162px;height:40px}

/* products */
.section-title{color:var(--orange);font-weight:700;font-size:40px}
.products-title{top:758px;width:1200px;text-align:center}
.product-card{top:866px;width:313px;height:416px;background:var(--grey);text-align:center}
.product-card .icon{position:absolute;left:114px;top:27px;width:85px;height:85px;border-radius:50%;background:var(--orange);display:flex;align-items:center;justify-content:center}
.product-card h3{position:absolute;top:128px;width:100%;color:var(--orange);font-size:25px;font-weight:600}
.product-card p{position:absolute;top:177px;left:40px;width:233px;font-size:20px;line-height:29px}
.pill{background:var(--orange);color:#fff;border-radius:16px;font-size:17px;font-weight:500;display:flex;align-items:center;justify-content:center}
.product-card .pill{position:absolute;left:93px;top:326px;width:127px;height:30px}

/* about */
.about{top:1404px;left:0;width:664px;height:559px;background:var(--dark);color:#fff}
.about h2{position:absolute;left:143px;top:110px;font-size:40px;font-weight:700}
.about p{position:absolute;left:138px;top:192px;width:490px;font-size:20px;line-height:29px;font-weight:500}
.about .btn-ghost{left:138px;top:441px;width:162px;height:40px;border-radius:20px}
.about-photo{top:1404px;left:664px;width:536px;height:559px;background:linear-gradient(160deg,#dfe4ea,#c4ccd6 55%,#8e97a3)}

/* projects */
.projects-title{left:93px;top:2027px}
.projects-lede{left:98px;top:2095px;width:560px;font-size:20px;line-height:29px}
.tab-list{left:90px;top:2217px;width:262px}
.tab{position:absolute;left:12px;font-size:20px;font-weight:600;white-space:nowrap}
.tab.active{left:0;top:0;width:260px;height:38px;background:var(--orange);color:#fff;border-radius:8px;padding-left:17px;line-height:38px}
.tab-rail{left:351px;top:2296px;width:3px;height:282px;background:linear-gradient(var(--orange) 58%,var(--blue) 58%)}
.project-card{top:2192px;left:433px;width:680px;height:418px;border-radius:90px 0 120px 0;background:radial-gradient(ellipse at 40% 20%,#2f6ab0,#0d2a5c 60%,#081a3c);overflow:hidden;color:#fff}
.project-card h3{position:absolute;left:47px;top:183px;font-size:26px;font-weight:700}
.project-card p{position:absolute;left:47px;top:230px;width:400px;font-size:20px;line-height:29px;font-weight:500}
.project-card .read{position:absolute;left:49px;top:345px;width:184px;height:44px;background:var(--orange);font-size:24px;font-weight:600;display:flex;align-items:center;justify-content:center;border-radius:3px}

/* contact */
.contact{top:2680px;left:0;width:1200px;height:535px;background:var(--grey)}
.contact-title{left:220px;top:2752px;font-size:42px}
.contact-item{left:220px;display:flex;gap:10px;font-size:19px;line-height:26px}
.contact-item svg{flex:none;margin-top:3px}
.socials{left:222px;top:3007px;display:flex;gap:9px}
.socials span{width:34px;height:34px;border-radius:50%;display:block}
.field{left:601px;width:397px;background:#fff;border:1px solid #ddd;font-size:17px;color:#666;padding:9px 16px}
.submit{left:601px;top:3012px;width:397px;height:46px;background:var(--orange);color:#fff;font-size:21px;font-weight:600;display:flex;align-items:center;justify-content:center}

/* footer */
.site-footer{top:3215px;left:0;width:1200px;height:642px;background:var(--footer);color:#fff}
.newsletter{top:3155px;left:126px;width:951px;height:170px;background:var(--orange-soft);border-radius:10px;color:#fff}
.newsletter h3{position:absolute;left:60px;top:40px;font-size:30px;font-weight:500}
.newsletter p{position:absolute;left:60px;top:82px;width:330px;font-size:15px;line-height:18px;font-weight:500}
.news-form{position:absolute;left:517px;top:57px;width:374px;height:60px;background:#fff;border:3px solid var(--orange);border-radius:30px}
.news-form span{position:absolute;left:22px;top:16px;font-size:15px;color:#999}
.news-form .pill{position:absolute;right:6px;top:6px;width:125px;height:42px;border-radius:21px;font-size:15px}
.foot-col{top:3425px;font-size:16px}
.foot-col h4{color:var(--orange);font-size:17px;font-weight:600;margin-bottom:22px}
.foot-col li{list-style:none;line-height:30px;font-weight:500}
.foot-about p{font-size:15px;line-height:24px;width:330px}
.foot-contact li{display:flex;gap:16px;line-height:19px;margin-bottom:22px;font-size:15px}
.foot-rule{top:3695px;left:0;width:1200px;height:1px;background:#333}
.to-top{top:3657px;left:1109px;width:62px;height:62px;border-radius:50%;background:var(--orange);display:flex;align-items:center;justify-content:center}
.site-footer .brand{left:60px;top:520px}
.copyright{left:465px;top:3737px;font-size:16px}
</style>
</head>
<body>

<header class="site-header abs">
  <div class="brand abs"><span class="dot"></span>CopperWren Works</div>
  <nav class="main-nav abs">
    <a class="active">Home</a><a>About us</a><a>Products</a><a>Projects</a><a>Contributions</a><a>News</a><a>Privacy</a>
  </nav>
</header>

<section class="hero abs" role="img" aria-label="Photo of hands typing on a laptop on a dark desk">
  <h1>LOREM IPSUM DOLOR SIT<br>AMET, IPSUM DOLOR</h1>
  <p>Lorem ipsum dolor sit amet, consectetur adipiscing elit, sed do eiusmod . Risus commodo viverra maecenas accumsan lacus vel facilisis.</p>
  <a class="btn-ghost abs">Read More</a>
</section>

<h2 class="section-title products-title abs">OUR PRODUCTS</h2>
<article class="product-card abs" style="left:87px">
  <div class="icon"><svg width="40" height="40" viewBox="0 0 40 40" fill="none" stroke="#fff" stroke-width="2.5"><circle cx="20" cy="20" r="15"/><path d="M5 20h30M20 5c6 5 6 25 0 30M20 5c-6 5-6 25 0 30"/></svg></div>
  <h3>COPPERWREN</h3>
  <p>Lorem ipsum dolor sit amet, consectetur adipiscing elit, sed do eiusmod tempor</p>
  <a class="pill">Read More</a>
</article>
<article class="product-card abs" style="left:444px">
  <div class="icon"><svg width="40" height="40" viewBox="0 0 40 40" fill="none" stroke="#fff" stroke-width="2.5"><path d="M12 34v-7c-4-3-6-7-5-12 2-8 13-10 19-5 4 3 5 8 3 12l3 5h-4v7h-7"/><circle cx="19" cy="16" r="4"/></svg></div>
  <h3>COPPERWREN</h3>
  <p>Lorem ipsum dolor sit amet, consectetur adipiscing elit, sed do eiusmod tempor</p>
  <a class="pill">Read More</a>
</article>
<article class="product-card abs" style="left:800px">
  <div class="icon"></div>
  <h3>COPPERWREN</h3>
  <p>Lorem ipsum dolor sit amet, consectetur adipiscing elit, sed do eiusmod tempor</p>
  <a class="pill">Read More</a>
</article>

<section class="about abs">
  <h2>ABOUT US</h2>
  <p>Lorem ipsum dolor sit amet, consectetur adipiscing elit, sed do eiusmod tempor incididunt ut labore et dolore magna aliqua. Quis ipsum suspendisse ultrices gravida. Risus commodo viverra maecenas accumsan lacus vel facilisis. ommodo viverra maecenas accumsan lacus vel facilisis.</p>
  <a class="btn-ghost abs">Read More</a>
</section>
<div class="about-photo abs" role="img" aria-label="Photo of a bright white desk with a laptop, tablet and lamp"></div>

<h2 class="section-title projects-title abs">Current Projects</h2>
<p class="projects-lede abs">Lorem ipsum dolor sit amet, consectetur adipiscing elit, sed do eiusmod tempor inci labore et dolore</p>
<div class="tab-list abs">
  <div class="tab active">Artificial Intelligenece</div>
  <div class="tab" style="top:73px">Extended Reality</div>
  <div class="tab" style="top:141px">Data Visualization</div>
  <div class="tab" style="top:201px">Artificial Intelligenece</div>
  <div class="tab" style="top:270px">Current Projects</div>
  <div class="tab" style="top:339px">Extended Reality</div>
</div>
<div class="tab-rail abs"></div>
<article class="project-card abs" role="img" aria-label="Blue network graphic illustrating artificial intelligence">
  <h3>ARTIFICIAL INTELIGENCE</h3>
  <p>Lorem ipsum dolor sit amet, consectetur adipiscing elit, sed do eiusmod tempor incididunt ut labore</p>
  <a class="read">READ MORE</a>
</article>

<section class="contact abs"></section>
<h2 class="section-title contact-title abs">Contact us</h2>
<div class="contact-item abs" style="top:2832px"><svg width="20" height="22" viewBox="0 0 24 24" fill="#ff8c00"><path d="M6.6 10.8a15 15 0 006.6 6.6l2.2-2.2c.3-.3.7-.4 1-.2 1.1.4 2.3.6 3.6.6.6 0 1 .4 1 1V20c0 .6-.4 1-1 1A17 17 0 013 4c0-.6.4-1 1-1h3.5c.6 0 1 .4 1 1 0 1.3.2 2.5.6 3.6.1.3 0 .7-.2 1z"/></svg>123-123-5555</div>
<div class="contact-item abs" style="top:2884px"><svg width="22" height="18" viewBox="0 0 24 18" fill="#ff8c00"><path d="M0 2l12 8 12-8V0H0zM0 4v14h24V4l-12 8z"/></svg>@infoeloremipsum.com</div>
<div class="contact-item abs" style="top:2937px"><svg width="20" height="26" viewBox="0 0 20 26" fill="#ff8c00"><path d="M10 0a10 10 0 0110 10c0 7-10 16-10 16S0 17 0 10A10 10 0 0110 0zm0 6a4 4 0 100 8 4 4 0 000-8z"/></svg>Lorem ipsum dolor sit amet,<br>consectetur&nbsp; dolor sit amet</div>
<div class="socials abs"><span style="background:#1da1f2"></span><span style="background:#c13584"></span><span style="background:#3b5998"></span></div>
<div class="field abs" style="top:2764px;height:46px">Enter your name</div>
<div class="field abs" style="top:2832px;height:46px">Enter your email</div>
<div class="field abs" style="top:2900px;height:95px">Message</div>
<a class="submit abs">Submit</a>

<footer class="site-footer abs">
  <div class="brand abs"><span class="dot"></span>CopperWren Works</div>
</footer>
<div class="newsletter abs">
  <h3>Newsletter Sign Up!</h3>
  <p>Lorem ipsum dolor sit amet, consectetur adipiscing elit, sed do eiusmod tempor</p>
  <div class="news-form"><span>Email here</span><a class="pill">SUMBIT</a></div>
</div>
<div class="foot-col foot-about abs" style="left:70px;color:#fff">
  <h4>About Us</h4>
  <p>Lorem Ipsum is simply dummy text of the printing and typesetting industry. Lorem Ipsum has been the industry's standard dummy text ever since the 1500s.</p>
</div>
<div class="foot-col abs" style="left:459px;color:#fff">
  <h4>Links</h4>
  <ul><li>About Us</li><li>Products</li><li>Projects</li><li>Contributions</li><li>News Privacy</li></ul>
</div>
<div class="foot-col abs" style="left:678px;color:#fff">
  <h4>Support</h4>
  <ul><li>FAQ</li><li>How it</li><li>Features</li><li>Contact</li><li>Reporting</li></ul>
</div>
<div class="foot-col foot-contact abs" style="left:910px;color:#fff">
  <h4 style="margin-left:4px">Contact</h4>
  <ul>
    <li><svg width="20" height="20" viewBox="0 0 24 24" fill="#ff8c00"><path d="M6.6 10.8a15 15 0 006.6 6.6l2.2-2.2c.3-.3.7-.4 1-.2 1.1.4 2.3.6 3.6.6.6 0 1 .4 1 1V20c0 .6-.4 1-1 1A17 17 0 013 4c0-.6.4-1 1-1h3.5c.6 0 1 .4 1 1 0 1.3.2 2.5.6 3.6.1.3 0 .7-.2 1z"/></svg><span>Phone Number<br>+012345679</span></li>
    <li><svg width="20" height="16" viewBox="0 0 24 18" fill="#ff8c00"><path d="M0 2l12 8 12-8V0H0zM0 4v14h24V4l-12 8z"/></svg><span>Email Address<br>info@yourdomain.com</span></li>
    <li><svg width="20" height="22" viewBox="0 0 20 26" fill="#ff8c00"><path d="M10 0a10 10 0 0110 10c0 7-10 16-10 16S0 17 0 10A10 10 0 0110 0zm0 6a4 4 0 100 8 4 4 0 000-8z"/></svg><span>Office Address<br>Your Address Is Here</span></li>
  </ul>
</div>
<div class="foot-rule abs"></div>
<a class="to-top abs"><svg width="24" height="14" viewBox="0 0 24 14" fill="none" stroke="#fff" stroke-width="3"><path d="M2 12L12 2l10 10"/></svg></a>
<p class="copyright abs" style="color:#fff">Copyright&nbsp; @2030. All Rights Reserved</p>

</body>
</html>
```